Create an awesome website for a medical clinic

This is a new website for a doctor's office. The site should be clean and modern, easy to navigate.

This is a wellness clinic, we want to help our clients have a healthy, active lifestyle. It should be friendly and inviting, and easy for them to call or schedule an appointment.

The site should be responsive and designed using the attached Bootstrap 3 PSD.

We will provide stock photos, until then please use stock photos from:

pictovault.net or
imagebarrow.net (preferred)

Some example sites of clean and modern designs that we like:

https://tarvelspine.example/
http://quellmarrow.example/
http://brisklyhale.example/

Also attached is a temporary logo you can use.

Reason: Thank you everyone for your great designs - we need a little more time so I'm extending the project.

Need extra days to review

Also, the colors in the new logo I just linked to are the final colors of the logo, so feel free to use any complimentary colors to it.

Hi everyone, The boss wants to change the layout of the site a little bit - here's the revised layout: https://www.filecrate.example/s/k9pz31xq7vn84te/notes%2011_29_2017.pdf?dl=0 And the graphic assets you can use are here: https://www.filecrate.example/s/k9pz31xq7vn84te/notes%2011_29_2017.pdf?dl=0 Feel free to change the background color of the "topbar", and change the icons of the "why people trust us" if you want, these are just temporary placeholders. Thanks for your patience and hard work!

Target Market(s)

People seeking medical treatment (wellness clinic)

Industry/Entity Type

Doctor

Number of Pages Required

1 page

Font styles to use
Sans Serif

Colors
0592cd
33a6d7
abd037
9bcb3c

Requirements
Must have
• The home page should have: a strong hero image/slideshow, clinic phone number should be prominent and at the top of the page (in the nav), a "what to expect" section (this is like a FAQs section - see attachment), and a strong call to action (a button to call or schedule an appointment).
• The what to expect section is useful so that prospective clients can determine if we're a good fit for them or not. It's a basic, first-step pre-qualification block of information.
• Social media icons which links to our social media profiles should be included.
Nice to have
• - Link to 3 most recent blog entries
• - Testimonials
• - How a multilevel nav menu looks.

```html
<!DOCTYPE html>
<html lang="en">
<head>
<meta charset="utf-8">
<title>Fernhall Medical Clinic</title>
<link href="https://fonts.googleapis.com/css2?family=Roboto:wght@300;400;500;700&display=swap" rel="stylesheet">
<style>
:root{
  --blue:#0592cd;
  --blue-light:#33a6d7;
  --green:#9bcb3c;
  --green-light:#abd037;
  --text:#6f747a;
  --text-soft:#a9adb2;
  --line:#c7e3f0;
  --info-bar:#656c75;
  --footer:#575d66;
  --bottom:#4a5058;
  --white:#ffffff;
}
*{box-sizing:border-box;margin:0;padding:0}
html,body{width:1200px;height:4548px;overflow:hidden}
body{position:relative;background:var(--white);font-family:'Roboto',sans-serif;color:var(--text)}
.abs{position:absolute}
.ph{position:absolute}

/* header */
.topbar-field{top:16px;height:24px;border:1px solid #d9dde1;border-radius:3px;font-size:11px;color:var(--text-soft);display:flex;align-items:center;gap:6px;padding:0 8px}
.topbar-field i{width:10px;height:10px;border-radius:2px;background:var(--blue);display:block}
.phone{top:12px;left:742px;display:flex;align-items:center;gap:10px;font-size:22px;font-weight:500;color:#444}
.phone .dot{width:26px;height:26px;border-radius:50%;background:var(--blue);display:flex;align-items:center;justify-content:center}
.social{top:14px;left:968px;display:flex;gap:8px}
.social span{width:24px;height:24px;background:var(--blue);border-radius:3px;display:block}
.nav{top:80px;display:flex;gap:22px;font-size:13px;color:#555;letter-spacing:.3px}
.brand{top:22px;left:0;width:1200px;text-align:center}
.brand .name{font-size:34px;font-weight:700;color:var(--green);letter-spacing:1px;line-height:1}
.brand .sub{font-size:11px;font-weight:700;color:var(--green);letter-spacing:1.5px;margin-top:2px}
.btn-form{top:142px;left:520px;width:160px;height:28px;background:var(--blue);color:var(--white);font-size:10px;font-weight:500;letter-spacing:.6px;display:flex;align-items:center;justify-content:center;border-radius:2px}

/* hero */
.hero{top:192px;left:0;width:1200px;height:470px;background:linear-gradient(180deg,#6b4a2c 0%,#c9782c 45%,#f0a43a 58%,#4b3220 75%,#2a1d14 100%);clip-path:polygon(0 0,100% 0,100% 86%,0 100%)}
.hero h1{position:absolute;top:126px;left:0;width:1200px;text-align:center;color:var(--white);font-size:38px;font-weight:500;line-height:1.35}
.hero-dots{top:616px;left:550px;display:flex;gap:40px}
.hero-dots span{width:34px;height:34px;background:#eee;border-radius:3px;display:block}

/* section titles */
.sec-title{left:0;width:1200px;text-align:center;font-size:27px;font-weight:500;color:#777}
.chev{left:588px}

/* trust cards */
.card{width:320px;height:240px;border:2px solid var(--line);display:flex;flex-direction:column;align-items:center;justify-content:flex-end;padding-bottom:40px;gap:30px}
.card p{font-size:15px;color:#888}

/* symptoms */
.symptom{width:228px}
.symptom .img{width:228px;height:196px;background:radial-gradient(circle at 50% 45%,#8fb7e6 0%,#3a5f94 55%,#1c2b44 100%)}
.symptom p{font-size:13px;color:#888;margin-top:10px}

/* appointment band */
.appt{top:2140px;left:0;width:1200px;height:600px;background:linear-gradient(100deg,#b9d9ec 0%,#6fb0d9 40%,#3e86bb 100%);clip-path:polygon(0 27%,100% 0,100% 73%,0 100%)}
.appt-title{top:2330px;left:612px;font-size:26px;color:var(--white);font-weight:500}
.appt-text{top:2380px;left:612px;width:440px;font-size:14px;line-height:1.6;color:#e8f3fa}
.btn-outline{top:2500px;left:612px;width:190px;height:30px;border:1px solid var(--white);color:var(--white);font-size:10px;letter-spacing:.6px;display:flex;align-items:center;justify-content:center}

/* about */
.about-title{top:2888px;left:100px;font-size:28px;font-weight:500;color:#777}
.about-text{top:2940px;left:100px;width:520px;font-size:14px;line-height:1.6;color:var(--text-soft)}

/* contact */
.contact-bg{top:3150px;left:0;width:1200px;height:600px;background:linear-gradient(90deg,#fff 0%,#e6e8eb 40%,#8b9199 75%,#6f757d 100%);clip-path:polygon(0 28%,100% 0,100% 100%,0 100%)}
.form-card{top:3150px;left:720px;width:312px;height:470px;background:var(--white);box-shadow:0 4px 18px rgba(0,0,0,.15);padding:28px 24px}
.form-card h3{font-size:20px;font-weight:400;color:#777;text-align:center;margin-bottom:24px}
.field{height:34px;border:1px solid #dde1e5;margin-bottom:14px;font-size:12px;color:var(--text-soft);padding:9px 10px}
.field.area{height:110px}
.btn-send{height:32px;background:var(--blue);color:var(--white);font-size:11px;display:flex;align-items:center;justify-content:center;margin-top:6px}

/* info bar */
.info-bar{top:3740px;left:0;width:1200px;height:120px;background:var(--info-bar)}
.info{top:3774px;display:flex;gap:14px;color:var(--white)}
.info .ic{width:40px;height:40px;border-radius:50%;display:flex;align-items:center;justify-content:center}
.info b{display:block;font-size:14px;font-weight:500}
.info small{font-size:12px;color:#d5d9de}

/* footer */
.footer{top:3860px;left:0;width:1200px;height:280px;background:var(--footer)}
.fcol{top:3880px;color:#cfd3d8;font-size:12px;line-height:1.75}
.fcol h4{font-size:14px;font-weight:500;color:var(--white);margin-bottom:10px}
.hours{display:grid;grid-template-columns:110px 90px}

/* map */
.map{top:4140px;left:0;width:1200px;height:360px;background:linear-gradient(135deg,#eceef0 0%,#dfe2e5 100%)}
.totop{top:4462px;left:560px;width:80px;height:40px;background:#7a8088;border-radius:40px 40px 0 0;display:flex;align-items:center;justify-content:center}

.bottom{top:4500px;left:0;width:1200px;height:48px;background:var(--bottom);color:#c9cdd2;font-size:12px;display:flex;align-items:center;justify-content:space-between;padding:0 100px}
.bottom .sq{display:flex;gap:8px}
.bottom .sq span{width:20px;height:20px;border:1px solid #c9cdd2;border-radius:3px;display:block}
</style>
</head>
<body>

<!-- header -->
<header>
  <div class="abs topbar-field" style="left:132px;width:128px"><i></i>info@fernhall.clinic</div>
  <div class="abs topbar-field" style="left:300px;width:140px"><i></i>Search this site</div>
  <div class="abs brand"><div class="name">FERNHALL</div><div class="sub">MEDICAL CLINIC</div></div>
  <div class="abs phone"><span class="dot"><svg width="14" height="14" viewBox="0 0 24 24"><path fill="#fff" d="M6.6 10.8a15 15 0 0 0 6.6 6.6l2.2-2.2c.3-.3.7-.4 1-.2 1.1.4 2.3.6 3.6.6.6 0 1 .4 1 1V20c0 .6-.4 1-1 1A17 17 0 0 1 3 4c0-.6.4-1 1-1h3.5c.6 0 1 .4 1 1 0 1.3.2 2.5.6 3.6.1.3 0 .7-.2 1z"/></svg></span>(555) 014-2290</div>
  <div class="abs social"><span></span><span></span><span></span></div>
  <nav class="abs nav" style="left:100px"><span>HOME</span><span>ABOUT US</span><span>OUR UNIQUE APPROACH</span></nav>
  <nav class="abs nav" style="left:800px"><span>NEW PATIENT CENTER</span><span>BLOG</span><span>CONTACT US</span></nav>
  <div class="abs btn-form">NEW PATIENT FORM</div>
</header>

<!-- hero -->
<section class="abs hero" role="img" aria-label="Photo of a person meditating on a hilltop at sunset">
  <h1>Focused on Providing 5 Star<br>Quality Medical Care</h1>
</section>
<div class="abs hero-dots"><span></span><span></span></div>

<!-- why trust -->
<h2 class="abs sec-title" style="top:786px">Why People Trust Us</h2>
<svg class="abs chev" style="top:834px" width="24" height="24" viewBox="0 0 24 24"><path d="M12 3v16M5 13l7 7 7-7" stroke="#7fc4e4" stroke-width="1.5" fill="none"/></svg>

<div class="abs card" style="top:928px;left:100px">
  <svg width="84" height="70" viewBox="0 0 84 70"><rect x="28" y="2" width="28" height="12" rx="3" fill="none" stroke="#555" stroke-width="4"/><rect x="2" y="12" width="80" height="56" rx="6" fill="#e0463c"/><path d="M36 26h12v10h10v12H48v10H36V48H26V36h10z" fill="#fff"/></svg>
  <p>A New Perspective on Health</p>
</div>
<div class="abs card" style="top:928px;left:440px">
  <svg width="84" height="76" viewBox="0 0 84 76"><rect x="10" y="4" width="50" height="66" fill="#f3f3f3" stroke="#bbb" stroke-width="2"/><path d="M18 18h34M18 28h34M18 38h26" stroke="#6aa8d8" stroke-width="3"/><rect x="50" y="40" width="28" height="16" rx="2" fill="#f2b84b"/></svg>
  <p>Our Mission &amp; Guiding Principles</p>
</div>
<div class="abs card" style="top:928px;left:780px">
  <svg width="84" height="76" viewBox="0 0 84 76"><path d="M42 72 8 38A20 20 0 0 1 42 12a20 20 0 0 1 34 26z" fill="#e8443a"/><path d="M10 38h18l6-12 8 24 6-12h24" stroke="#fff" stroke-width="4" fill="none"/></svg>
  <p>Gentle &amp; Precise Care</p>
</div>
<div class="abs card" style="top:1192px;left:100px">
  <svg width="74" height="76" viewBox="0 0 74 76"><rect x="4" y="12" width="66" height="60" rx="4" fill="#fbe3c4" stroke="#f0a44a" stroke-width="3"/><rect x="4" y="12" width="66" height="16" fill="#f0a44a"/><path d="M20 4v14M54 4v14" stroke="#555" stroke-width="4"/><path d="M22 46l10 10 20-20" stroke="#e8643a" stroke-width="4" fill="none"/></svg>
  <p>Fewer Treatments - Lasting Results</p>
</div>
<div class="abs card" style="top:1192px;left:440px">
  <div role="img" aria-label="Icon of a medical imaging scanner" style="width:110px;height:70px;background:linear-gradient(90deg,#9aa4b0,#e8e8e8 60%,#f2c14e)"></div>
  <p>Advanced Imaging</p>
</div>
<div class="abs card" style="top:1192px;left:780px">
  <div role="img" aria-label="Icon of a healthcare worker" style="width:70px;height:74px;border-radius:35px 35px 8px 8px;background:linear-gradient(180deg,#f2c14e,#4a90c8)"></div>
  <p>Healthcare Team</p>
</div>

<!-- symptoms -->
<h2 class="abs sec-title" style="top:1524px">Common Symptoms Seen in our Office</h2>
<svg class="abs chev" style="top:1574px" width="24" height="24" viewBox="0 0 24 24"><path d="M12 3v16M5 13l7 7 7-7" stroke="#7fc4e4" stroke-width="1.5" fill="none"/></svg>

<div class="abs symptom" style="top:1668px;left:100px"><div class="img" role="img" aria-label="X-ray style image of a head with headache highlighted"></div><p>Headache &amp; Migraines</p></div>
<div class="abs symptom" style="top:1668px;left:357px"><div class="img" role="img" aria-label="X-ray style image of neck and shoulders"></div><p>Neck Pain &amp; Shoulder Pain</p></div>
<div class="abs symptom" style="top:1668px;left:614px"><div class="img" role="img" aria-label="X-ray style image of lower back and hips"></div><p>Low Back Pain &amp; Hip Pain &amp; Sciatica</p></div>
<div class="abs symptom" style="top:1668px;left:872px"><div class="img" role="img" aria-label="X-ray style image of the brain"></div><p>Dizziness &amp; Vertigo &amp; Meniere</p></div>
<div class="abs symptom" style="top:1936px;left:100px"><div class="img" role="img" aria-label="X-ray style image of the face and jaw"></div><p>Trigeminal Neuralgia &amp; Face Pain</p></div>
<div class="abs symptom" style="top:1936px;left:357px"><div class="img" role="img" aria-label="X-ray style image of the spine"></div><p>Fibromyalgia &amp; Chronic Fatigue</p></div>

<!-- appointment -->
<section class="abs appt"></section>
<div class="ph" role="img" aria-label="Photo of a smiling female doctor holding a clipboard" style="top:2290px;left:220px;width:300px;height:450px;background:linear-gradient(180deg,#d9c2a8 0%,#f4f6f8 40%,#cfd8e0 100%);clip-path:polygon(0 0,100% 0,100% 82%,0 100%)"></div>
<h2 class="abs appt-title">Book an Appointment</h2>
<p class="abs appt-text">Lorem ipsum dolor sit amet consectetur adipiscing elit sed do eiusmod tempor incididunt ut labore et dolore magna aliqua ut enim ad minim veniam quis nostrud exercitation ullamco laboris nisi ut aliquip ex ea commodo.</p>
<div class="abs btn-outline">BOOK NOW</div>

<!-- about -->
<h2 class="abs about-title">About us</h2>
<p class="abs about-text">Lorem ipsum dolor sit amet consectetur adipiscing elit sed do eiusmod tempor incididunt ut labore et dolore magna aliqua ut enim ad minim veniam quis nostrud exercitation ullamco laboris nisi ut aliquip ex ea commodo consequat duis aute irure dolor in reprehenderit in voluptate velit esse cillum dolore eu fugiat nulla pariatur excepteur sint occaecat.</p>
<div class="ph" role="img" aria-label="Photo of a doctor talking with a patient" style="top:2812px;left:700px;width:400px;height:228px;background:linear-gradient(90deg,#e9eef2 0%,#c7d3dd 50%,#8c9aa8 100%)"></div>

<!-- contact -->
<section class="abs contact-bg"></section>
<div class="ph" role="img" aria-label="Photo of a smiling doctor pointing towards the message form" style="top:3230px;left:100px;width:420px;height:510px;background:linear-gradient(180deg,#b08a6a 0%,#f3f5f7 35%,#dfe6ec 100%)"></div>
<form class="abs form-card">
  <h3>Send us a Message</h3>
  <div class="field">Name</div>
  <div class="field">Email Address</div>
  <div class="field">Phone</div>
  <div class="field area">Your Message</div>
  <div class="btn-send">Send Message</div>
</form>

<!-- info bar -->
<div class="abs info-bar"></div>
<div class="abs info" style="left:350px"><span class="ic" style="background:var(--blue-light)"><svg width="18" height="18" viewBox="0 0 24 24"><path fill="#fff" d="M12 2a7 7 0 0 0-7 7c0 5 7 13 7 13s7-8 7-13a7 7 0 0 0-7-7zm0 9.5A2.5 2.5 0 1 1 12 6.5a2.5 2.5 0 0 1 0 5z"/></svg></span><div><b>Our Address</b><small>1250 W Elm Rd, Suite 4</small></div></div>
<div class="abs info" style="left:612px"><span class="ic" style="background:var(--green)"><svg width="18" height="18" viewBox="0 0 24 24"><circle cx="12" cy="12" r="9" stroke="#fff" stroke-width="2" fill="none"/><path d="M12 7v5l3 3" stroke="#fff" stroke-width="2" fill="none"/></svg></span><div><b>Open Hours</b><small>Mon - Friday: 8AM - 6PM</small></div></div>
<div class="abs info" style="left:872px"><span class="ic" style="background:var(--blue-light)"><svg width="18" height="18" viewBox="0 0 24 24"><path fill="#fff" d="M6.6 10.8a15 15 0 0 0 6.6 6.6l2.2-2.2c.3-.3.7-.4 1-.2 1.1.4 2.3.6 3.6.6.6 0 1 .4 1 1V20c0 .6-.4 1-1 1A17 17 0 0 1 3 4c0-.6.4-1 1-1h3.5c.6 0 1 .4 1 1 0 1.3.2 2.5.6 3.6.1.3 0 .7-.2 1z"/></svg></span><div><b>Give us a Call</b><small>(555) 014-2290</small></div></div>

<!-- footer -->
<footer class="abs footer"></footer>
<div class="abs fcol" style="left:100px;width:200px"><h4>About us</h4>Caring for your whole health with gentle, precise treatment plans built around you.</div>
<div class="abs fcol" style="left:350px"><h4>Navigation</h4>Home<br>About us<br>Our Unique Approach<br>New Patient Center<br>Blog<br>Contact us</div>
<div class="abs fcol" style="left:600px"><h4>Services</h4>Health Exams<br>Lab Tests<br>Imaging<br>Follow Care</div>
<div class="abs fcol" style="left:860px"><h4>Working Hours</h4>
  <div class="hours"><span>Monday</span><span>8AM - 6PM</span><span>Tuesday</span><span>8AM - 6PM</span><span>Wednesday</span><span>8AM - 6PM</span><span>Thursday</span><span>8AM - 6PM</span><span>Friday</span><span>8AM - 6PM</span><span>Saturday</span><span>Closed</span><span>Sunday</span><span>Closed</span></div>
</div>

<!-- map -->
<div class="abs map" role="img" aria-label="Street map of the area around the clinic"></div>
<svg class="abs" style="top:4254px;left:586px" width="28" height="40" viewBox="0 0 24 34"><path fill="var(--blue-light)" d="M12 0a12 12 0 0 0-12 12c0 9 12 22 12 22s12-13 12-22A12 12 0 0 0 12 0zm0 17a5 5 0 1 1 0-10 5 5 0 0 1 0 10z"/></svg>
<div class="abs totop"><svg width="18" height="12" viewBox="0 0 18 12"><path d="M2 10 9 3l7 7" stroke="#fff" stroke-width="2" fill="none"/></svg></div>

<div class="abs bottom"><span>© 2017 All right reserved</span><div class="sq"><span></span><span></span></div></div>

</body>
</html>
```